GUARANTEED! Simple website for independent event planner and consultant...

I need a website that is no more than 5 or 6 pages to illustrate who I am and what I can offer to groups who book hotels for meetings and conferences. I have 20 years of experience planning meetings within hotels and I am now ready to go out on my own and help clients choose venues, negotiate contracts and plan effective meetings. I will focus on clients planning meetings in the mountains of Colorado but I am willing to travel as well. I want to work with a person who is collaborative and can direct me on what they need to move the project along quickly. I already have my logo, a hosting site and work e-mail address. Also, I recently hired a photographer to do head shots. Lastly, it important for me to be able to talk on the phone or skype with this person, as needed and I must be able to make changes to my site down the road when necessary...

Target Market(s)

Corporate Groups

Industry/Entity Type

Event Planning

Coding

Coded - Design and coding required

Number of Pages Required

5+ page

Font styles to use
Sans Serif

Requirements
Must have
• About me page, event planning services offered page, task force and consulting work page, testimonials page, page for blogs, page to contact me/request a proposal. May need advice on what else I need...
Nice to have
• I want it to look sharp and professional. I want people to look at my site and know immediately that they can trust me and the work I can do.
• I don't want it to look like it is over the top as I am not a HUGE company but I do want it to be professional and easy to view and navigate.
Should not have
• Bright colors
• My logo is bright orange and black. I have also used dark grey and orange. See below:
• Orange:
• C = 0
• M = 64
• Y = 100
• K = 0
• Gray:
• C = 67
• M = 60
• Y = 59
• K = 45
• Font: Gotham Book and Gotham Bold

```html
<!DOCTYPE html>
<html lang="en">
<head>
<meta charset="utf-8">
<title>Harlow Event Management</title>
<link href="https://fonts.googleapis.com/css2?family=Montserrat:wght@400;500;600;700&family=Open+Sans:wght@400;600&display=swap" rel="stylesheet">
<style>
:root{
  --orange:#f47b20;
  --dark:#333536;
  --darker:#262728;
  --grey-bg:#ececec;
  --text:#555;
  --white:#fff;
}
*{box-sizing:border-box;margin:0;padding:0}
html,body{width:1200px;height:3084px;overflow:hidden}
body{font-family:"Open Sans",Arial,sans-serif;color:var(--text);background:var(--white);position:relative}
h1,h2,h3,.brand,.nav a{font-family:"Montserrat",Arial,sans-serif}

/* top bar */
.topbar{position:absolute;top:0;left:0;width:1200px;height:30px;z-index:3;display:flex;justify-content:flex-end;align-items:center;padding-right:40px;gap:26px}
.topbar span{font-size:12px;color:#fff;display:flex;align-items:center;gap:7px}
.topbar-back{position:absolute;top:0;right:0;width:430px;height:30px;background:var(--dark);z-index:2;clip-path:polygon(24px 0,100% 0,100% 100%,0 100%)}

/* header */
.header{position:absolute;top:0;left:0;width:1200px;height:96px;z-index:1;background:var(--white)}
.brand{position:absolute;left:150px;top:48px;color:var(--orange);font-weight:600;font-size:18px;line-height:1;white-space:nowrap}
.nav{position:absolute;left:430px;top:52px;display:flex;gap:20px;white-space:nowrap}
.nav a{font-size:12px;color:#444;text-decoration:none;font-weight:500;padding-bottom:6px}
.nav a.active{color:var(--orange);border-bottom:2px solid var(--orange)}

/* hero */
.hero{position:absolute;top:96px;left:0;width:1200px;height:496px;background:linear-gradient(180deg,#7d848b 0%,#5c6166 55%,#3d4145 100%)}
.hero::after{content:"";position:absolute;inset:0;background:rgba(20,20,20,.25)}
.hero-frame{position:absolute;left:390px;top:175px;width:420px;height:150px;z-index:1}
.hero h1{position:absolute;left:0;top:203px;width:1200px;text-align:center;color:#fff;font-size:38px;font-weight:600;line-height:1.25;z-index:1}
.hero .arrow{position:absolute;top:237px;width:26px;height:26px;border-radius:50%;background:rgba(255,255,255,.35);z-index:1;display:flex;align-items:center;justify-content:center}

/* section titles */
.title{display:inline-block;position:relative;color:var(--orange);font-size:28px;font-weight:600;padding:4px 10px}
.title svg{position:absolute;left:0;top:0}

/* about */
.about{position:absolute;top:592px;left:0;width:1200px;height:568px;background:var(--white)}
.about .title{position:absolute;left:158px;top:112px}
.about .copy{position:absolute;left:166px;top:185px;width:510px;font-size:13px;line-height:1.62;color:#555}
.about .copy p{margin-bottom:14px}
.btn{display:inline-block;background:var(--orange);color:#fff;font-family:"Montserrat",Arial,sans-serif;font-size:13px;font-weight:600;padding:10px 20px}
.about .btn{position:absolute;left:166px;top:400px}
.portrait-frame{position:absolute;left:740px;top:140px;width:290px;height:290px;border:1px solid #ccc;padding:9px}
.portrait{width:100%;height:100%;background:linear-gradient(160deg,#e9e9e9,#bdbdbd 60%,#4d4d4d)}

/* services */
.services{position:absolute;top:1160px;left:0;width:1200px;height:520px;background:linear-gradient(180deg,#4e5257,#2b2d30 60%,#1f2022)}
.services::after{content:"";position:absolute;inset:0;background:rgba(0,0,0,.3)}
.services .title{position:absolute;left:497px;top:34px;z-index:1}
.service-list{position:absolute;top:162px;left:180px;width:840px;display:flex;justify-content:space-between;z-index:1}
.service{width:170px;text-align:center;color:#fff}
.service .icon{width:110px;height:110px;border-radius:50%;background:#fff;margin:0 auto 18px;display:flex;align-items:center;justify-content:center;border:5px solid rgba(255,255,255,.5);background-clip:padding-box}
.service h3{font-size:14px;font-weight:600;line-height:1.35}

/* gallery */
.gallery{position:absolute;top:1680px;left:0;width:1200px;height:660px}
.gallery .title{position:absolute;left:490px;top:80px}
.photo{position:absolute;border:5px solid #fff;box-shadow:0 0 0 1px #d6d6d6}
.photo div{width:100%;height:100%}

/* testimonials & blog */
.feedback{position:absolute;top:2340px;left:0;width:1200px;height:420px;background:var(--grey-bg)}
.feedback .title{font-size:24px}
.t-col{position:absolute;left:160px;top:70px;width:470px}
.b-col{position:absolute;left:668px;top:70px;width:380px}
.dots{position:absolute;top:18px;right:0;display:flex;gap:6px}
.dots i{width:12px;height:12px;border-radius:50%;background:#ccc;display:block}
.dots i.on{background:var(--orange)}
.quote{margin-top:40px;background:#fff;padding:28px 30px 24px 60px;position:relative;font-size:12px;line-height:1.65;font-style:italic;color:#777}
.quote .mark{position:absolute;left:20px;top:18px;color:#d0d0d0;font-size:46px;font-family:Georgia,serif;font-style:normal;line-height:1}
.quote .who{margin-top:12px;text-align:center;color:var(--orange);font-style:normal;font-weight:600}
.post{display:flex;gap:14px;margin-top:22px}
.post:first-of-type{margin-top:40px}
.post .date{flex:none;width:52px;height:52px;background:var(--orange);color:#fff;text-align:center;font-family:"Montserrat",Arial,sans-serif;font-size:11px;font-weight:600;line-height:1.2;padding-top:11px}
.post .date b{display:block;font-size:15px}
.post p{font-size:11.5px;line-height:1.5;color:#666}
.post p strong{color:#333}

/* footer */
.footer{position:absolute;top:2760px;left:0;width:1200px;height:280px;background:var(--dark);color:#ccc}
.footer h3{color:var(--orange);font-size:15px;font-weight:600;margin-bottom:14px}
.f-col{position:absolute;top:36px}
.links li{list-style:none;font-size:12px;line-height:1.85}
.links li::before{content:"› ";color:var(--orange)}
.contact-row{display:flex;gap:12px;font-size:12px;line-height:1.5;margin-bottom:14px;align-items:flex-start}
.contact-row svg{flex:none;margin-top:2px}
.form label{display:block;font-size:11px;margin-bottom:3px}
.form .field{width:150px;height:22px;background:#fff;margin-bottom:8px}
.form .area{height:38px}
.form .send{display:inline-block;background:var(--orange);color:#fff;font-size:11px;padding:5px 14px;font-family:"Montserrat",Arial,sans-serif;font-weight:600}
.f-brand{position:absolute;left:860px;top:72px;color:var(--orange);font-family:"Montserrat",Arial,sans-serif;font-weight:600;font-size:18px;line-height:1;white-space:nowrap}
.social{position:absolute;left:868px;top:152px;display:flex;gap:14px}
.social i{width:20px;height:20px;border-radius:50%;background:#555;display:block}
.copyright{position:absolute;top:3040px;left:0;width:1200px;height:44px;background:var(--darker);color:#aaa;font-size:12px;text-align:center;line-height:44px}
</style>
</head>
<body>

<div class="topbar-back"></div>
<div class="topbar">
  <span><svg width="13" height="10" viewBox="0 0 13 10"><rect x=".5" y=".5" width="12" height="9" fill="none" stroke="#f47b20"/><path d="M.5 .5l6 5 6-5" fill="none" stroke="#f47b20"/></svg>info@harloweventmanagement.com</span>
  <span><svg width="11" height="11" viewBox="0 0 11 11"><path d="M2 0l2 3-1 1.5c.8 1.6 1.9 2.7 3.5 3.5L8 7l3 2-1 2C5 11 0 6 0 1z" fill="#f47b20"/></svg>303-555-0148</span>
</div>

<header class="header">
  <div class="brand">Harlow Event Management</div>
  <nav class="nav">
    <a class="active">Home</a><a>About Me</a><a>Event Planning Services</a><a>Task Force And Consulting</a><a>Testimonials</a><a>Blog</a><a>Contact Me</a>
  </nav>
</header>

<section class="hero" role="img" aria-label="Photo of business guests networking at a hotel conference reception">
  <svg class="hero-frame" viewBox="0 0 420 150" width="420" height="150">
    <path d="M0 40V0h40M380 0h40v40M420 110v40h-40M40 150H0v-40" fill="none" stroke="#f47b20" stroke-width="4"/>
  </svg>
  <h1>Event Planner And Consultant<br>Working Independently</h1>
  <div class="arrow" style="left:112px"><svg width="8" height="12"><path d="M7 1L2 6l5 5" fill="none" stroke="#fff" stroke-width="2"/></svg></div>
  <div class="arrow" style="right:112px"><svg width="8" height="12"><path d="M1 1l5 5-5 5" fill="none" stroke="#fff" stroke-width="2"/></svg></div>
</section>

<section class="about">
  <h2 class="title"><svg width="140" height="46"><path d="M14 2H2v42h12M126 2h12v42h-12" fill="none" stroke="#f47b20" stroke-width="2"/></svg>About Me</h2>
  <div class="copy">
    <p>Harlow Event Management specializes in event management for associations, corporations, not-for-profit companies and personal social events of all sizes in the state of Colorado.</p>
    <p>After a successful 20+ year career coordinating events in the resort community of Vail I am now providing her skills on the other side of the table. When you hire Harlow Event Management you are hiring a company who is intimately familiar with the inner workings of hotels, resorts and off-site hospitality venues. You will be working with an event professional who can assist with selecting the right venue and negotiating a contract that benefits you and your company.</p>
  </div>
  <span class="btn">Read More</span>
  <div class="portrait-frame"><div class="portrait" role="img" aria-label="Head shot of the event planner"></div></div>
</section>

<section class="services" role="img" aria-label="Dark photo of a meeting audience in a conference hall">
  <h2 class="title"><svg width="206" height="46"><path d="M14 2H2v42h12M192 2h12v42h-12" fill="none" stroke="#f47b20" stroke-width="2"/></svg>Our Services</h2>
  <div class="service-list">
    <div class="service"><div class="icon"><svg width="44" height="44" viewBox="0 0 44 44"><rect x="6" y="8" width="32" height="30" rx="3" fill="#f47b20"/><rect x="10" y="16" width="24" height="18" fill="#fff"/><rect x="12" y="4" width="4" height="8" fill="#f47b20"/><rect x="28" y="4" width="4" height="8" fill="#f47b20"/><path d="M16 25l4 4 8-8" fill="none" stroke="#f47b20" stroke-width="3"/></svg></div><h3>Site Selection and<br>Venue Sourcing</h3></div>
    <div class="service"><div class="icon"><svg width="44" height="44" viewBox="0 0 44 44"><rect x="9" y="4" width="26" height="36" rx="2" fill="#f47b20"/><path d="M14 13h16M14 19h16M14 25h10" stroke="#fff" stroke-width="2.5"/><path d="M22 34l6-6 4 4-6 6h-4z" fill="#fff"/></svg></div><h3>Contract<br>Negotiation</h3></div>
    <div class="service"><div class="icon"><svg width="48" height="40" viewBox="0 0 48 40"><path d="M6 28a18 18 0 0136 0z" fill="#f47b20"/><rect x="2" y="30" width="44" height="4" rx="2" fill="#f47b20"/><circle cx="24" cy="7" r="3" fill="#f47b20"/></svg></div><h3>Food and<br>Beverage</h3></div>
    <div class="service"><div class="icon"><svg width="44" height="44" viewBox="0 0 44 44"><rect x="8" y="6" width="28" height="34" rx="2" fill="#f47b20"/><rect x="16" y="3" width="12" height="7" rx="2" fill="#f47b20" stroke="#fff" stroke-width="2"/><path d="M13 18l2 2 4-4M13 27l2 2 4-4" fill="none" stroke="#fff" stroke-width="2"/><path d="M22 19h9M22 28h9" stroke="#fff" stroke-width="2.5"/></svg></div><h3>Agenda Creation and<br>Program Planning</h3></div>
  </div>
</section>

<section class="gallery">
  <h2 class="title"><svg width="220" height="46"><path d="M14 2H2v42h12M206 2h12v42h-12" fill="none" stroke="#f47b20" stroke-width="2"/></svg>Work Gallery</h2>
  <div class="photo" style="left:168px;top:140px;width:332px;height:228px"><div role="img" aria-label="Photo of a business meeting around a conference table" style="background:linear-gradient(135deg,#c9d3dc,#8e9aa5)"></div></div>
  <div class="photo" style="left:520px;top:140px;width:280px;height:228px"><div role="img" aria-label="Photo of colleagues sharing a meal at a restaurant" style="background:linear-gradient(135deg,#d9c3a8,#8f7a66)"></div></div>
  <div class="photo" style="left:820px;top:140px;width:212px;height:228px"><div role="img" aria-label="Photo of guests networking at an evening event" style="background:linear-gradient(135deg,#9a8c80,#3f3b38)"></div></div>
  <div class="photo" style="left:168px;top:380px;width:204px;height:228px"><div role="img" aria-label="Photo of business people in a conference hall" style="background:linear-gradient(135deg,#b7bfc8,#5d6670)"></div></div>
  <div class="photo" style="left:388px;top:380px;width:212px;height:228px"><div role="img" aria-label="Photo of meeting attendees reviewing notes" style="background:linear-gradient(135deg,#c4b8ab,#6c6258)"></div></div>
  <div class="photo" style="left:616px;top:380px;width:188px;height:228px"><div role="img" aria-label="Photo of professionals shaking hands" style="background:linear-gradient(135deg,#d0d3d6,#7b8088)"></div></div>
  <div class="photo" style="left:820px;top:380px;width:212px;height:228px"><div role="img" aria-label="Photo of a banquet dinner setting" style="background:linear-gradient(135deg,#b99c7c,#5a4636)"></div></div>
</section>

<section class="feedback">
  <div class="t-col">
    <h2 class="title" style="padding-left:0">Client Testimonials</h2>
    <div class="dots"><i></i><i class="on"></i></div>
    <div class="quote"><span class="mark">“</span>Working with Harlow made our annual leadership retreat effortless. Every detail was handled before we even thought to ask, and the contract terms she secured saved our association a significant amount. I would not plan another conference without her guidance and calm experience.
      <div class="who">Mr. Daniel Ostrom</div></div>
  </div>
  <div class="b-col">
    <h2 class="title" style="padding-left:0">Latest Blog Posts</h2>
    <div class="dots"><i></i><i class="on"></i></div>
    <div class="post"><div class="date"><b>12</b>MAY</div><p><strong>Choosing the right mountain venue for your group.</strong> Space, access and season all shape the meeting your attendees will remember.</p></div>
    <div class="post"><div class="date"><b>28</b>APR</div><p><strong>Five contract clauses every planner should review.</strong> Attrition, cancellation and food minimums can quietly raise your final bill.</p></div>
    <div class="post"><div class="date"><b>09</b>APR</div><p><strong>Building an agenda that keeps people engaged.</strong> Balance sessions, breaks and networking so energy stays high all day.</p></div>
  </div>
</section>

<footer class="footer">
  <div class="f-col" style="left:168px">
    <h3>Quick Links</h3>
    <ul class="links"><li>Home</li><li>About Me</li><li>Event Planning Services</li><li>Task Force And Consulting</li><li>Testimonials</li><li>Blog</li><li>Contact Me</li></ul>
  </div>
  <div class="f-col" style="left:368px">
    <h3>Contact Detail</h3>
    <div class="contact-row"><svg width="12" height="16" viewBox="0 0 12 16"><path d="M6 0a6 6 0 016 6c0 4-6 10-6 10S0 10 0 6a6 6 0 016-6z" fill="#f47b20"/><circle cx="6" cy="6" r="2" fill="#333"/></svg><span>Harlow Event Management<br>Vail, Colorado 81657</span></div>
    <div class="contact-row"><svg width="12" height="12" viewBox="0 0 11 11"><path d="M2 0l2 3-1 1.5c.8 1.6 1.9 2.7 3.5 3.5L8 7l3 2-1 2C5 11 0 6 0 1z" fill="#f47b20"/></svg><span>303-555-0148</span></div>
    <div class="contact-row"><svg width="13" height="10" viewBox="0 0 13 10"><rect x=".5" y=".5" width="12" height="9" fill="#f47b20"/><path d="M.5 .5l6 5 6-5" fill="none" stroke="#333"/></svg><span>info@harloweventmanagement.com</span></div>
  </div>
  <div class="f-col form" style="left:650px">
    <h3>Quick Enquiry</h3>
    <label>Email</label><div class="field"></div>
    <label>Phone</label><div class="field"></div>
    <label>Message</label><div class="field area"></div>
    <span class="send">Submit</span>
  </div>
  <div class="f-brand">Harlow Event Management</div>
  <div class="social"><i></i><i></i><i></i><i></i></div>
</footer>
<div class="copyright">Copyright © 2017 Harlow Event Management. All Rights Reserved</div>

</body>
</html>
```